WP website design (Brenwick)

We need a wordpress design that will incorporate a professional color scheme with company logo in a clean layout. The design needs to consider that this will be developed on a responsive theme. Colors are undetermined - can use a dark red - logo is black so creative use of colors will be important. Client wants a 'modern' look.

Industry/Entity Type

It Company

Font styles to use
Serif
Sans Serif

Colors

Designer to choose colors to be used in the design.

Requirements
Must have
• Navigation: 1) Home 2) Auctions 3) Auction Services 4) Our Company 5) Contact Us

Site will have a slideshow element and the following widgets: 1) Featured Auctions 2) Testimonials blog widget 3) 'Auction Alerts' email sign up 4) Featured Videos

In the footer, there will be smaller company logo, the affiliations logo, and contact info below:
Brenwick Auction & Realty” • 3817 Marlow Creek Road •
Ashgrove, AR 72958 • (479) 582-3107 • tbrenwick@quelmail.com.
Nice to have
• - Site will have drop-down menus - please indicate the styling, for instance the dropdown menus 1) Upcoming Auctions 2) Past Auctions under the 'Auctions' link

```html
<!DOCTYPE html>
<html lang="en">
<head>
<meta charset="utf-8">
<title>Brenwick Auction &amp; Realty</title>
<link href="https://fonts.googleapis.com/css2?family=Kaushan+Script&family=PT+Serif&family=Roboto:wght@400;500;700&family=Source+Sans+3:wght@400;600;700&display=swap" rel="stylesheet">
<style>
:root{
  --red:#a81414;
  --red-dark:#8e0f0f;
  --red-bright:#c4161c;
  --black:#0b0b0b;
  --panel:#121212;
  --white:#ffffff;
  --line:#6e1010;
}
*{box-sizing:border-box;margin:0;padding:0}
html,body{width:883px;height:1200px;overflow:hidden}
body{position:relative;background:var(--black);font-family:"Source Sans 3",Arial,sans-serif;color:var(--white)}
.abs{position:absolute}

/* header */
.site-header{left:0;top:0;width:883px;height:90px;background:linear-gradient(#ffffff,#ececec)}
.brand{left:78px;top:28px;font-weight:700;font-size:28px;color:#111;letter-spacing:-.3px;display:flex;align-items:center;gap:9px}
.brand .mark{width:12px;height:12px;background:#111}

/* nav */
.main-nav{left:0;top:90px;width:883px;height:36px;background:linear-gradient(#c01a1a,var(--red-dark));border-bottom:3px solid #111}
.main-nav ul{list-style:none;display:flex;height:100%;padding-left:62px}
.main-nav li{font-weight:600;font-size:12px;text-transform:uppercase;letter-spacing:.2px;padding:0 24px;display:flex;align-items:center;border-right:1px solid #d34242}
.main-nav li:last-child{border-right:none}
.dropdown{left:158px;top:130px;width:144px;background:var(--red);font-size:12px;box-shadow:0 2px 4px rgba(0,0,0,.3);z-index:3}
.dropdown div{height:26px;padding-left:16px;display:flex;align-items:center}
.dropdown .active{background:#111}

/* hero */
.hero-band{left:0;top:129px;width:883px;height:245px;background:linear-gradient(#ffffff,#e9e9e9)}
.slider{left:78px;top:153px;width:474px;height:196px;background:linear-gradient(#7fa9d8 0%,#c9dbee 35%,#8b3a2a 55%,#6a2a20 78%,#5e7e3a 92%)}
.slider-next{left:518px;top:165px}
.slider-dots{left:290px;top:320px;display:flex;gap:8px}
.slider-dots span{width:11px;height:11px;border-radius:50%;background:#fff}
.slider-dots .on{background:var(--red-bright);border:1px solid #fff}
.signup{left:575px;top:153px;width:234px;height:190px;background:var(--red);padding:18px 19px}
.script{font-family:"Kaushan Script",cursive}
.signup h2{font-weight:400;font-size:24px;margin-bottom:10px}
.signup p{font-size:11px;line-height:15px;margin-bottom:10px}
.signup .field{width:181px;height:25px;background:#fff;color:#777;font-size:10px;padding:6px 9px;margin-bottom:19px}
.signup .btn{display:inline-block;background:#111;font-weight:600;font-size:12px;padding:5px 13px;border:1px solid #333}

/* intro */
.welcome{left:80px;top:404px;font-size:23px;font-weight:400}
.tagline{left:80px;top:442px;color:var(--red-bright);font-size:14px}

/* auction cards */
.auction-card{width:452px;height:229px;border:1px solid var(--red);background:var(--panel)}
.auction-card .head{height:33px;background:linear-gradient(#c01a1a,var(--red-dark));font-family:"Roboto",sans-serif;font-weight:700;font-size:12.5px;padding:11px 16px;border-radius:4px 4px 0 0}
.auction-card .thumb{left:25px;top:43px;width:118px;height:78px;background:linear-gradient(#c4ccd4 0%,#aab3b8 38%,#6f8a4c 45%,#5a7a3a 100%);box-shadow:0 2px 6px rgba(0,0,0,.6)}
.auction-card .btn{left:53px;width:76px;height:24px;background:var(--red);border-radius:3px;font-family:"Roboto",sans-serif;font-size:10px;display:flex;align-items:center;gap:6px;padding-left:9px}
.auction-card .info{left:164px;top:52px;width:275px;font-family:"Roboto",sans-serif;font-size:10px;line-height:14px}
.info .date{font-family:"Source Sans 3",sans-serif;font-weight:700;font-size:13px;letter-spacing:.6px;margin-bottom:6px}
.info .bill{color:var(--red-bright);font-weight:700;font-size:11px;padding-left:78px;margin:6px 0 8px}
.info b{font-weight:500}
.info .pin{display:flex;gap:4px;align-items:center}

/* sidebar */
.video{left:576px;top:404px;width:232px;height:165px;background:linear-gradient(90deg,#d6d6d0 0%,#9c9b94 40%,#5c5a52 70%,#8a8f8a 100%)}
.video .bar{left:0;bottom:0;width:232px;height:12px;background:#e8e8e8;border-top:1px solid #999}
.video .progress{left:20px;top:4px;width:95px;height:3px;background:#777}
.video .progress i{display:block;width:58px;height:3px;background:var(--red-bright)}
.widget{left:577px;width:231px;border:1px solid var(--line);background:var(--panel)}
.widget .head{height:33px;background:linear-gradient(#c01a1a,var(--red-dark));font-family:"PT Serif",serif;font-size:21px;padding:4px 15px;border-radius:4px 4px 0 0}
.featured{top:603px;height:233px;text-align:center;font-family:"Roboto",sans-serif;font-size:9.5px;line-height:15px}
.featured .thumb{width:131px;height:79px;margin:6px auto 10px;border:2px solid #fff;background:linear-gradient(#d2d8de 0%,#8fa0a8 40%,#6f7f55 75%,#4d6b34 100%)}
.testimonials{top:866px;height:212px}
.quote{display:flex;gap:9px;padding:0 10px 0 14px;font-size:10px;line-height:13.5px}
.quote .avatar{flex:none;width:41px;height:37px;background:linear-gradient(#e8e6e0,#9e9a92)}
.testimonials hr{border:none;border-top:1px solid #3a3a3a;margin:10px 9px}
.signoff{text-align:right;padding-right:19px;color:var(--red-bright);font-style:italic;font-weight:700;font-size:11px;margin-top:18px}

/* footer */
.site-footer{left:0;top:1107px;width:883px;height:93px;background:var(--red)}
.footer-info{left:79px;top:14px;font-family:"Roboto",sans-serif;font-size:10px;line-height:17.6px}
.footer-brand{left:422px;top:33px;font-weight:700;font-size:22px;display:flex;align-items:center;gap:7px}
.footer-brand .mark{width:10px;height:10px;background:#fff}
.affiliations{left:620px;top:28px;display:flex;gap:10px}
.affiliations span{width:34px;height:34px;background:#fff;opacity:.92}
.affiliations .round{border-radius:50%}
</style>
</head>
<body>

<header class="site-header abs">
  <div class="brand abs"><span class="mark"></span>Brenwick Auction &amp; Realty</div>
</header>

<nav class="main-nav abs">
  <ul>
    <li>Home</li><li>Auctions</li><li>Auction Services</li><li>Our Company</li><li>Contact Us</li>
  </ul>
</nav>

<section class="hero-band abs"></section>
<div class="dropdown abs">
  <div>Upcoming Auction</div>
  <div class="active">Past Auction</div>
</div>
<div class="slider abs" role="img" aria-label="Slideshow photo of a large red brick house with lawn"></div>
<svg class="slider-next abs" width="20" height="20" viewBox="0 0 20 20">
  <circle cx="10" cy="10" r="10" fill="#111"/>
  <path d="M5 13c1-4 4-5 7-5V5.5l4 4-4 4V11c-3 0-5 .5-7 2z" fill="#fff"/>
</svg>
<div class="slider-dots abs"><span></span><span class="on"></span><span></span><span></span></div>

<aside class="signup abs">
  <h2 class="script">Email Signup</h2>
  <p>Please join our free mailing list to get auction alerts for upcoming events.</p>
  <div class="field">Enter Your Email</div>
  <span class="btn">Subscribe</span>
</aside>

<h1 class="welcome abs script">Welcome to Brenwick Auction and Realty</h1>
<p class="tagline abs">Serving Western Arkansas and Eastern Oklahoma since 1982</p>

<article class="auction-card abs" style="left:80px;top:494px">
  <div class="head">ART, FURNITURE AND ACCESSORIES ONLINE AUCTION</div>
  <div class="thumb abs" role="img" aria-label="Photo of open grassland tract"></div>
  <div class="btn abs" style="top:138px"><svg width="13" height="12" viewBox="0 0 13 12"><rect x="1" y="1" width="9" height="7" rx="2" fill="#cfe3f5"/><rect x="4" y="4" width="8" height="7" rx="2" fill="#fff"/></svg>Details</div>
  <div class="btn abs" style="top:171px"><svg width="13" height="12" viewBox="0 0 13 12"><rect x="0" y="1" width="13" height="10" fill="#e8d27a"/><rect x="2" y="3" width="9" height="6" fill="#4d8a3c"/></svg>Photos</div>
  <div class="info abs">
    <div class="date">THURSDAY, AUGUST 21ST AT 10:00 A.M.</div>
    <div>Selling 3120 Acres of land in tracts of 2590 Acres<br>&amp; 560 Acres</div>
    <div class="bill">Click here to view Sale Bill!</div>
    <div><b>LIVE OFF-SITE AUCTION</b></div>
    <div><b>Auction Location:</b></div>
    <div class="pin"><svg width="9" height="11" viewBox="0 0 9 11"><path d="M4.5 0A4 4 0 0 1 8.5 4c0 3-4 7-4 7S.5 7 .5 4a4 4 0 0 1 4-4z" fill="#c4161c"/><circle cx="4.5" cy="4" r="1.5" fill="#fff"/></svg>118 N Cedar Lane, Dovershire, OK 73911</div>
    <div><b>Property Location:</b></div>
    <div class="pin"><svg width="9" height="11" viewBox="0 0 9 11"><path d="M4.5 0A4 4 0 0 1 8.5 4c0 3-4 7-4 7S.5 7 .5 4a4 4 0 0 1 4-4z" fill="#c4161c"/><circle cx="4.5" cy="4" r="1.5" fill="#fff"/></svg>118 N Cedar Lane, Dovershire, OK 73911</div>
    <div style="padding-left:49px">08/21/14 at 10:00 AM CDT</div>
  </div>
</article>

<article class="auction-card abs" style="left:78px;top:755px">
  <div class="head">ART, FURNITURE AND ACCESSORIES ONLINE AUCTION</div>
  <div class="thumb abs" role="img" aria-label="Photo of open grassland tract"></div>
  <div class="btn abs" style="top:138px"><svg width="13" height="12" viewBox="0 0 13 12"><rect x="1" y="1" width="9" height="7" rx="2" fill="#cfe3f5"/><rect x="4" y="4" width="8" height="7" rx="2" fill="#fff"/></svg>Details</div>
  <div class="btn abs" style="top:171px"><svg width="13" height="12" viewBox="0 0 13 12"><rect x="0" y="1" width="13" height="10" fill="#e8d27a"/><rect x="2" y="3" width="9" height="6" fill="#4d8a3c"/></svg>Photos</div>
  <div class="info abs">
    <div class="date">THURSDAY, AUGUST 21ST AT 10:00 A.M.</div>
    <div>Selling 3120 Acres of land in tracts of 2590 Acres<br>&amp; 560 Acres</div>
    <div class="bill">Click here to view Sale Bill!</div>
    <div><b>LIVE OFF-SITE AUCTION</b></div>
    <div><b>Auction Location:</b></div>
    <div class="pin"><svg width="9" height="11" viewBox="0 0 9 11"><path d="M4.5 0A4 4 0 0 1 8.5 4c0 3-4 7-4 7S.5 7 .5 4a4 4 0 0 1 4-4z" fill="#c4161c"/><circle cx="4.5" cy="4" r="1.5" fill="#fff"/></svg>118 N Cedar Lane, Dovershire, OK 73911</div>
    <div><b>Property Location:</b></div>
    <div class="pin"><svg width="9" height="11" viewBox="0 0 9 11"><path d="M4.5 0A4 4 0 0 1 8.5 4c0 3-4 7-4 7S.5 7 .5 4a4 4 0 0 1 4-4z" fill="#c4161c"/><circle cx="4.5" cy="4" r="1.5" fill="#fff"/></svg>118 N Cedar Lane, Dovershire, OK 73911</div>
    <div style="padding-left:49px">08/21/14 at 10:00 AM CDT</div>
  </div>
</article>

<div class="video abs" role="img" aria-label="Featured video still of auctioneers speaking to a crowd outdoors">
  <svg class="abs" style="left:91px;top:44px" width="50" height="50" viewBox="0 0 50 50">
    <circle cx="25" cy="25" r="25" fill="rgba(20,20,20,.8)"/>
    <path d="M19 14l18 11-18 11z" fill="#fff"/>
  </svg>
  <div class="bar abs">
    <svg class="abs" style="left:4px;top:2px" width="7" height="8" viewBox="0 0 7 8"><path d="M0 0l7 4-7 4z" fill="#333"/></svg>
    <div class="progress abs"><i></i></div>
  </div>
</div>

<aside class="widget featured abs">
  <div class="head" style="text-align:left">Featured Auctions</div>
  <div style="margin-top:12px;font-weight:500">13.35 ACRES OF PRIME DEVELOP<br>&amp; 33RD STREET</div>
  <div class="thumb" role="img" aria-label="Photo of a farmhouse with auction crowd"></div>
  <div>LOTS 13 &amp; 14 FOR SALE, MAPLECROFT<br>IOWA<br>Third Street, Maplecroft, IA 52704</div>
</aside>

<aside class="widget testimonials abs">
  <div class="head">Testimonial Blog</div>
  <div class="quote" style="margin-top:25px"><div class="avatar" role="img" aria-label="Reviewer portrait"></div><p>Contrary to popular belief, Lorem Ipsum is not simply random text. It a piece of classical.</p></div>
  <hr>
  <div class="quote"><div class="avatar" role="img" aria-label="Reviewer portrait"></div><p>Contrary to popular belief, Lorem Ipsum is not simply random text. It a piece of classical.</p></div>
  <div class="signoff">..Dale Fennimore</div>
</aside>

<footer class="site-footer abs">
  <div class="footer-info abs">
    Brenwick Auction &amp; Realty”<br>
    • 3817 Marlow Creek Road •<br>
    Ashgrove, AR 72958 • (479) 582-3107 • tbrenwick@quelmail.com<br>
    Copyright © 2014: Brenwick Auction &amp; Realty Inc.
  </div>
  <div class="footer-brand abs"><span class="mark"></span>Brenwick</div>
  <div class="affiliations abs"><span></span><span></span><span></span><span class="round"></span></div>
</footer>

</body>
</html>
```